Income Tax Flyer - Updates Needed

Just need to update this flyer design and give it a new look. We would like to keep all the same wording but make it stand out a little more. Our selling point is the "Same Day Tax Advance up to $6,000"

Industry/Entity Type

Lending, Small Loans, Tax Services, Title Loans, Personal Loans

```html
<!DOCTYPE html>
<html lang="en">
<head>
<meta charset="utf-8">
<title>Easy Advance Tax Flyer</title>
<link href="https://fonts.googleapis.com/css2?family=Anton&family=Montserrat:wght@600;700&family=Quicksand:wght@500&display=swap" rel="stylesheet">
<style>
  :root{
    --green-dark:#12532e;
    --green-mid:#0b6b2c;
    --green-bright:#07921f;
    --panel-left:#124f2f;
    --panel-right:#078a2a;
    --red:#d42a30;
    --black:#050505;
    --white:#ffffff;
    --ink:#1d1d1d;
    --page:#ffffff;
  }
  html,body{margin:0;padding:0;width:1200px;height:1200px;overflow:hidden;background:var(--page);}
  .canvas{position:relative;width:1200px;height:1200px;}
  .flyer{position:absolute;left:270px;top:127px;width:667px;height:932px;overflow:hidden;background:var(--white);}
  .flyer-bg{position:absolute;inset:0;}
  .brand{position:absolute;left:0;top:58px;width:266px;text-align:center;
    font-family:"Montserrat",sans-serif;font-weight:700;color:var(--green-dark);font-size:20px;line-height:1.15;letter-spacing:.5px;}
  .feature-panel{position:absolute;left:21px;top:0;width:221px;height:807px;}
  .feature{position:absolute;left:34px;width:150px;}
  .feature-badge{position:absolute;left:21px;width:106px;height:106px;border-radius:50%;background:var(--white);
    box-sizing:border-box;padding:5px;z-index:2;}
  .feature-badge svg{display:block;width:96px;height:96px;}
  .feature-card{position:absolute;left:0;width:150px;height:78px;background:var(--white);border-radius:12px;
    box-shadow:0 3px 8px rgba(0,0,0,.25);display:flex;align-items:flex-end;justify-content:center;box-sizing:border-box;padding-bottom:14px;
    font-family:"Quicksand",sans-serif;font-weight:500;font-size:14.5px;line-height:1.3;color:var(--ink);text-align:center;}
  .headline{position:absolute;left:262px;width:405px;top:400px;text-align:center;font-family:"Anton",sans-serif;line-height:1;}
  .headline .line-1{display:block;font-size:46px;color:var(--green-dark);letter-spacing:-.5px;transform:scaleY(1.05);}
  .headline .line-2{display:block;font-size:58px;color:var(--green-mid);margin-top:4px;letter-spacing:-1px;}
  .headline .line-3{display:block;font-size:72px;color:var(--green-mid);margin-top:0;}
  .offer{position:absolute;left:262px;width:405px;top:642px;text-align:center;color:var(--white);}
  .offer-lead{font-family:"Montserrat",sans-serif;font-weight:600;font-size:19.5px;letter-spacing:.8px;}
  .offer-name{font-family:"Anton",sans-serif;font-size:31px;margin-top:2px;letter-spacing:.3px;}
  .contact-button{position:absolute;left:249px;top:751px;width:178px;height:39px;box-sizing:border-box;border:4px solid var(--black);
    border-radius:20px;background:var(--white);color:var(--red);font-family:"Montserrat",sans-serif;font-weight:700;font-size:15px;
    display:flex;align-items:center;justify-content:center;letter-spacing:.3px;}
  .contact-line{position:absolute;color:var(--white);font-family:"Montserrat",sans-serif;font-weight:700;font-size:15.5px;letter-spacing:.6px;
    transform:translateX(-50%);white-space:nowrap;}
</style>
</head>
<body>
<div class="canvas">
  <div class="flyer">
    <svg class="flyer-bg" width="667" height="932" viewBox="0 0 667 932">
      <defs>
        <linearGradient id="photoTone" x1="0" y1="0" x2="1" y2="1">
          <stop offset="0" stop-color="#cfcbc6"/>
          <stop offset=".45" stop-color="#e9e2da"/>
          <stop offset="1" stop-color="#8f8378"/>
        </linearGradient>
        <linearGradient id="panelTone" x1="0" y1="0" x2="1" y2="0">
          <stop offset=".45" stop-color="var(--panel-left)"/>
          <stop offset="1" stop-color="var(--panel-right)"/>
        </linearGradient>
      </defs>
      <rect x="0" y="0" width="667" height="400" fill="url(#photoTone)" role="img" aria-label="Photo of two smiling women in white tops in a bright office"/>
      <path d="M0,268 C150,330 260,372 330,356 C450,330 560,295 667,262 L667,932 L0,932 Z" fill="var(--black)"/>
      <path d="M0,285 C150,347 260,390 330,374 C450,350 560,318 667,286 L667,932 L0,932 Z" fill="var(--green-bright)"/>
      <path d="M0,298 C150,362 260,400 330,392 C460,376 560,340 667,306 L667,932 L0,932 Z" fill="var(--white)"/>
      <rect x="0" y="621" width="667" height="200" fill="var(--red)"/>
      <path d="M0,785 Q350,660 667,778 L667,932 L0,932 Z" fill="var(--white)"/>
      <path d="M0,827 Q350,730 667,827 L667,932 L0,932 Z" fill="var(--black)"/>
      <path d="M0,0 H263 V142 L133,195 L0,142 Z" fill="var(--white)"/>
      <path d="M21,150 Q80,172 125,192 Q133,196 141,192 Q190,170 242,150 V777 Q242,807 212,807 H51 Q21,807 21,777 Z" fill="url(#panelTone)"/>
    </svg>

    <div class="brand">Keystone<br>Financial Group</div>

    <div class="feature-panel">
      <div class="feature" style="top:0">
        <div class="feature-badge" style="top:231px">
          <svg viewBox="0 0 96 96" fill="none" stroke="var(--green-dark)" stroke-width="2.2" stroke-linecap="round">
            <circle cx="48" cy="48" r="44" stroke-width="6"/>
            <circle cx="48" cy="52" r="22"/><circle cx="48" cy="52" r="16"/>
            <rect x="42" y="22" width="12" height="5" rx="2"/><path d="M48 27v3M31 35l-3-3M65 35l3-3"/>
            <path d="M52 47c-2-2-8-2-8 1s8 2 8 6-6 4-8 1M48 43v18"/>
          </svg>
        </div>
        <div class="feature-card" style="top:325px">Available In<br>24 Hours or Less</div>
      </div>
      <div class="feature" style="top:0">
        <div class="feature-badge" style="top:415px">
          <svg viewBox="0 0 96 96" fill="none" stroke="var(--green-dark)" stroke-width="2.2" stroke-linecap="round">
            <circle cx="48" cy="48" r="44" stroke-width="6"/>
            <path d="M58 36a20 20 0 1 0-18 24"/>
            <path d="M44 68V42a4 4 0 0 1 8 0v14l8 2a6 6 0 0 1 4 7l-2 6a8 8 0 0 1-8 5h-2a10 10 0 0 1-8-5l-4-6"/>
            <path d="M41 30c-2-2-7-1-7 1s7 2 7 5-5 3-7 1M37 26v16"/>
          </svg>
        </div>
        <div class="feature-card" style="top:508px">Choose Your<br>Loan Amount</div>
      </div>
      <div class="feature" style="top:0">
        <div class="feature-badge" style="top:602px">
          <svg viewBox="0 0 96 96" fill="none" stroke="var(--green-dark)" stroke-width="2.2" stroke-linecap="round">
            <circle cx="48" cy="48" r="44" stroke-width="6"/>
            <rect x="40" y="20" width="26" height="42" rx="3"/>
            <circle cx="53" cy="41" r="6"/>
            <path d="M30 70l-6-8 8-14 8-4 8 6-4 6-6-2M36 70l10-6"/>
          </svg>
        </div>
        <div class="feature-card" style="top:690px">Quick and<br>Easy</div>
      </div>
    </div>

    <h1 class="headline" style="margin:0;font-weight:400">
      <span class="line-1">APPLY HER FOR</span>
      <span class="line-2">$5.000-$6.000</span>
      <span class="line-3">TODAY</span>
    </h1>

    <div class="offer">
      <div class="offer-lead">File your taxes and apply for an</div>
      <div class="offer-name">Easy Advance!</div>
    </div>

    <div class="contact-button">Contact Us Today!</div>
    <div class="contact-line" style="left:338px;top:813px">Phone Number</div>
    <div class="contact-line" style="left:152px;top:874px">Address line 1</div>
    <div class="contact-line" style="left:335px;top:874px">Address line 2</div>
    <div class="contact-line" style="left:518px;top:874px">Address line 3</div>
  </div>
</div>
</body>
</html>
```